BrXpertz Business Cards for SME Experts

We need a business card for a new company based in Clearwater FL called Kestrel of Merit. KoM is your access to on-demand subject matter experts. The final design should be very clean communicating innovation and expertise. Our logo design is attached.

The Information Age has affected the workforce in that automation and computerization have resulted in higher productivity coupled with net job loss of many knowledgeable employees. Combined with the creation of the internet and search capabilities, the disintermediation of the value chain of Subject Matter Experts (SME) has happened. We no longer need to work through traditional consulting firms for all consulting needs, instead the direct access to the SME, through a leaner and lower cost model is what the market is demanding.
BrXpertz is a new marketplace to buy consulting services. The business model is that all consultants (subject matter experts) can become a consulting resource in the marketplace following our guidelines. The consumer can now easily access consultants that they could not find easily before.
In much the way an Zyla car can be identified and requested, so can a BrXpertz Consultant. Each consultant can be identified by: location, expertise, billing rate, and prior experience rating.
By seamlessly connecting consultants to requesters through a new Kestrel of Merit marketplace, you now will have an easy to use and quicker turnaround to request and staff your consulting needs. Leveraging the KoM app, you can access the subject matter expert you need for your business requirement.

Target Market(s)

Small and medium sized companies; non-profits

Industry/Entity Type

Business Consultant

Contact Information for Business Card

Name
website
email address
Logo
mailing address (debating if I really need...)
twitter
LinkedIn

Requirements
Must have
• the logo I have included in the design; want the colors to be consistent with the logo design

```html
<!DOCTYPE html>
<html lang="en">
<head>
<meta charset="UTF-8">
<title>Kestrel of Merit – Business Card</title>
<link rel="stylesheet" href="https://fonts.googleapis.com/css2?family=Open+Sans:ital,wght@0,400;0,600;0,700;1,400&display=swap">
<style>
  :root {
    --page: #e8e9eb;
    --card: #f3f3f5;
    --navy: #151d57;
    --teal: #1f8fb6;
    --teal-back: #1a8cb5;
    --ink: #2c3350;
    --white: #ffffff;
  }
  * { margin: 0; padding: 0; box-sizing: border-box; }
  html, body {
    width: 1105px; height: 1200px; overflow: hidden;
    background: var(--page);
    font-family: "Open Sans", Arial, sans-serif;
  }
  .card {
    position: absolute; left: 179px;
    width: 747px; height: 427px;
    overflow: hidden;
  }
  .card--front { top: 119px; background: var(--card); }
  .card--back { top: 637px; background: var(--teal-back); }

  .band { position: absolute; top: 48px; height: 101px; }
  .band--navy { left: 0; width: 563px; background: var(--navy); }
  .band--teal { left: 563px; right: 0; background: var(--teal); }

  .holder { position: absolute; left: 47px; top: 73px; color: var(--white); }
  .holder__name { font-size: 26px; font-weight: 700; line-height: 32px; }
  .holder__role { font-size: 18px; font-weight: 600; line-height: 24px; }

  .mark-circle {
    position: absolute; left: 514px; top: 46px;
    width: 104px; height: 104px; border-radius: 50%;
    background: var(--white); border: 5px solid var(--navy);
  }
  .brand-name {
    position: absolute; right: 57px; top: 160px;
    font-size: 28px; font-weight: 600; color: var(--navy);
    letter-spacing: 0.5px;
  }

  .contact { position: absolute; left: 47px; top: 320px; list-style: none; }
  .contact__item {
    display: flex; align-items: center; gap: 8px;
    font-size: 19px; color: var(--ink); line-height: 29px;
  }
  .contact__icon { width: 16px; height: 16px; flex: none; }

  .social { position: absolute; left: 624px; top: 345px; display: flex; gap: 3px; }
  .social__dot { width: 34px; height: 34px; border-radius: 50%; }
  .social__dot--one { background: var(--teal); }
  .social__dot--two { background: #1b6fa8; }

  .back-name {
    position: absolute; left: 0; right: 0; top: 176px;
    text-align: center; font-size: 44px; font-weight: 600;
    letter-spacing: 1px; color: var(--white);
  }
  .back-url {
    position: absolute; left: 0; right: 0; top: 352px;
    text-align: center; font-size: 19px; font-style: italic;
    letter-spacing: 3px; color: var(--white);
  }
</style>
</head>
<body>
  <section class="card card--front">
    <div class="band band--navy"></div>
    <div class="band band--teal"></div>
    <div class="holder">
      <p class="holder__name">Dana Whitfield</p>
      <p class="holder__role">Consultant</p>
    </div>
    <div class="mark-circle"></div>
    <p class="brand-name">Kestrel of Merit</p>
    <ul class="contact">
      <li class="contact__item">
        <svg class="contact__icon" viewBox="0 0 16 16"><rect x="1" y="3" width="14" height="10" fill="#151d57"/><path d="M1 3 L8 9 L15 3" fill="none" stroke="#f3f3f5" stroke-width="1.4"/></svg>
        Dana@KestrelofMerit.com
      </li>
      <li class="contact__item">
        <svg class="contact__icon" viewBox="0 0 16 16"><circle cx="8" cy="8" r="7" fill="#151d57"/><path d="M1 8 H15 M8 1 C4.5 5 4.5 11 8 15 M8 1 C11.5 5 11.5 11 8 15" fill="none" stroke="#f3f3f5" stroke-width="1"/></svg>
        KestrelofMerit.com
      </li>
    </ul>
    <div class="social">
      <span class="social__dot social__dot--one"></span>
      <span class="social__dot social__dot--two"></span>
    </div>
  </section>

  <section class="card card--back">
    <p class="back-name">Kestrel of Merit</p>
    <p class="back-url">www.KestrelofMerit.com</p>
  </section>
</body>
</html>
```